" MAIOR PARTE DO ATENDIMENTO SERÁ ONLINE, PODENDO OPTAR POR VISITAR AS FAZENDAS OU NÃO. DEVIDO O ATENDIMENTO AOS CLIENTES SER DE FORMA DIGITAL, MARCAMOS REUNIÃO ATRAVÉS DE VÍDEO CONFERÊNCIA, ASSIM TIRANDO SUAS DÚVIDAS E EXPLICANDO OS SERVIÇOS FORNECIDOS... TODAS AS INFORMAÇÕES OBTIDAS EM CONVERSA COM O CLIENTE SÃO UNIFICADAS COM AS INFORMAÇÕES QUE OBTEMOS ATRAVÉS DE IMAGENS DE SATÉLITE, E ATRAVÉS DE UMA RELATÓRIO CONSEGUIMOS EXPLICAR COMO ESTÁ A SUA FAZENDA, QUAL É O MELHOR MÉTODO DE MANEJO PARA A SAFRA, SE HÁ OU NÃO ÁREAS DEGRADADAS, EXPLICAMOS PARA ELE, QUAIS AS QUANTIDADE E QUAIS OS LOCAIS DEVERÃO RECEBER APLICAÇÃO DE ADUBO. A AGRICULTURA DE PRECISÃO NÃO É UM APARELHO ELA É UMA TÉCNICA PARA OTIMIZARMOS OS CUSTOS. DEIXAMOS DE TRATAR UMA PROPRIEDADE DE FORMA GERAL, E TRATAMOS CADA TALHÃO OU CADA PASTO DE FORMA DIFERENTE, DE ACORDO COM SUA NECESSIDADE, ASSIM DIMINUINDO CUSTOS E MELHORANDO A PRODUÇÃO DA PROPRIEDADE, E CONSEQUENTEMENTE, MELHORANDO O RETORNO FINANCEIRO DO PRODUTOR RURAL. "

```html
<!DOCTYPE html>
<html lang="pt-BR">
<head>
<meta charset="UTF-8">
<title>VERDA — Envelope</title>
<link href="https://fonts.googleapis.com/css2?family=Michroma&family=Montserrat:wght@400;500&display=swap" rel="stylesheet">
<style>
  :root {
    --bg: #b5b5b5;
    --paper: #ffffff;
    --forest: #0f2f2c;
    --gold: #b08d3c;
    --gold-light: #d9bf7a;
    --gold-dark: #7a5f22;
    --ink: #3a3a3a;
    --label: #222222;
  }
  * { margin: 0; padding: 0; box-sizing: border-box; }
  html, body { width: 1200px; height: 1200px; overflow: hidden; }
  body { background: var(--bg); position: relative; font-family: "Montserrat", sans-serif; }
  .sheet-label {
    position: absolute; left: 26px; top: 78px;
    font-size: 22px; letter-spacing: 1px; color: var(--label);
  }
  .envelope { position: absolute; left: 0; top: 0; width: 1200px; height: 1200px; }
  .flap {
    position: absolute; left: 192px; top: 252px; width: 391px; height: 56px;
    background: linear-gradient(90deg, var(--gold-dark), var(--gold-light) 45%, var(--gold) 70%, var(--gold-dark));
    clip-path: polygon(0 0, 100% 0, 100% 100%, 0 100%, 9% 0);
  }
  .back-panel {
    position: absolute; left: 192px; top: 307px; width: 391px; height: 653px;
    background: var(--paper);
  }
  .back-panel .watermark {
    position: absolute; left: 0; top: 40px; width: 391px; height: 440px;
    background: linear-gradient(160deg, rgba(0,0,0,0.015), rgba(0,0,0,0.04));
  }
  .front-panel {
    position: absolute; left: 583px; top: 252px; width: 391px; height: 679px;
    background: var(--forest);
  }
  .gold-edge {
    position: absolute; left: 583px; top: 928px; width: 391px; height: 12px;
    background: linear-gradient(90deg, var(--gold-dark), var(--gold-light) 40%, var(--gold) 80%, var(--gold-light));
    clip-path: polygon(0 0, 100% 0, 100% 40%, 0 100%);
  }
  .brand-name {
    font-family: "Michroma", sans-serif; color: var(--paper);
    letter-spacing: 10px; font-weight: 400;
  }
  .brand-tagline {
    font-family: "Montserrat", sans-serif; color: var(--gold);
    letter-spacing: 2.6px; text-transform: uppercase; font-weight: 500;
  }
  .front-brand { position: absolute; left: 660px; top: 550px; }
  .front-brand .brand-mark {
    display: inline-block; width: 28px; height: 28px; background: var(--gold);
    vertical-align: middle; margin-right: 14px;
  }
  .front-brand .brand-name { font-size: 40px; vertical-align: middle; }
  .front-brand .brand-tagline { font-size: 11px; margin: 10px 0 0 44px; }
  .back-brand { position: absolute; left: 24px; top: 430px; }
  .back-brand .brand-mark {
    display: inline-block; width: 14px; height: 14px; background: var(--gold);
    vertical-align: middle; margin-right: 7px;
  }
  .back-brand .brand-name { font-size: 19px; letter-spacing: 4px; color: var(--forest); vertical-align: middle; }
  .back-brand .brand-tagline { font-size: 5px; letter-spacing: 1.2px; margin: 3px 0 0 22px; }
  .contact-list { position: absolute; left: 24px; top: 486px; list-style: none; }
  .contact-list li {
    font-size: 8px; color: var(--ink); line-height: 1.35; margin-bottom: 9px;
    display: flex; align-items: flex-start; gap: 6px;
  }
  .contact-list svg { flex: none; margin-top: 1px; }
</style>
</head>
<body>
  <div class="sheet-label">ENVELOPE</div>
  <div class="envelope">
    <div class="flap"></div>
    <section class="back-panel">
      <div class="watermark" role="img" aria-label="Faint large brand symbol decoration"></div>
      <div class="back-brand">
        <span class="brand-mark"></span><span class="brand-name">VERDA</span>
        <div class="brand-tagline">Agricultura de Precisão</div>
      </div>
      <ul class="contact-list">
        <li>
          <svg width="7" height="7" viewBox="0 0 10 10"><path d="M2 1h2l1 2.5-1.3 1a5 5 0 0 0 2.8 2.8l1-1.3L10 7v2a1 1 0 0 1-1 1A9 9 0 0 1 0 2a1 1 0 0 1 1-1z" fill="#c0392b"/></svg>
          <span>(00) 0000-0000 / 00000-0000</span>
        </li>
        <li>
          <svg width="7" height="7" viewBox="0 0 10 10"><rect x="0" y="2" width="10" height="6" fill="#c0392b"/><path d="M0 2l5 3.5L10 2" stroke="#fff" fill="none"/></svg>
          <span>contato@verdaagro.com.br</span>
        </li>
        <li>
          <svg width="7" height="7" viewBox="0 0 10 10"><circle cx="5" cy="5" r="4.5" fill="#c0392b"/></svg>
          <span>www.verdaagro.com.br</span>
        </li>
        <li>
          <svg width="7" height="9" viewBox="0 0 10 13"><path d="M5 0a5 5 0 0 1 5 5c0 3.5-5 8-5 8S0 8.5 0 5a5 5 0 0 1 5-5z" fill="#c0392b"/><circle cx="5" cy="5" r="1.8" fill="#fff"/></svg>
          <span>Rua das Palmeiras, 120, Centro<br>CEP 00000-000 - Cidade-SP</span>
        </li>
      </ul>
    </section>
    <section class="front-panel"></section>
    <div class="gold-edge"></div>
    <div class="front-brand">
      <span class="brand-mark"></span><span class="brand-name">VERDA</span>
      <div class="brand-tagline">Agricultura de Precisão</div>
    </div>
  </div>
</body>
</html>
```